依頼詳細
■デザインのみになります。コーディング・設置は必要ありません。

ターゲットの方々が経営者や弁護士・医師の方々ですので、シックな雰囲気や高級感のあるテイストを希望しています。あまりごちゃごちゃしない方がいいです。そしてPC表示とスマートフォン表示は別のものを用意していただきたいと思っています。その辺りは以下のサイトを参照してください。

https://ki-gakuin.tokyo/lp1/

ファッション系のサービスなので、デザインにも、そこそここだわりたいと思っています。指標となるデザインは以下を参照してください。このようなテイストが個人的に好みです。あくまで参考程度に。

https://www.velmorine.com/
https://www.jobvantari.com/user/landing/general01
https://shigoto-meijin.jp/

それではみなさんからのご提案を楽しみにしております。どうぞ宜しくお願いいたします。※デザインのみになります。コーディングは必要ありません。
サイトURL
http://kaderiko.com/
ページ数
5ページ
希望イメージ
シンプル 複雑
単色 カラフル
暗い 明るい
日常 高級
遊び心 厳粛
未来的 伝統的
女性的 男性的
希望する色
青系、茶系、グレー系
納品ファイル
• フォトショップ形式 (.psd)
• PNG形式 (.png)
補足説明
・ホームページとスマートフォンでデザインが最適化されることを望んでいます。
・原稿は「添付ファイル」を参照してください。
・写真素材はこちらからダウンロードをお願いします。
http://22.fairudepo.nu/0617-b5f38392b646e45670ce877556e4cad98
■LPは縦長の1ページでお願いします
■文章量は添付ファイルをご確認ください
■ページ数が5ページとなっていますが、制作は縦長の1ページでお願いします。それなりに文章量がありますので、5ページという形で表現しています。
写真素材は以下からダウンロードしてください。http://26.fairudepo.nu/0624-bc3dae55294a2553bb88fed86e6d836ae(ギガファイル便6月24日まで)
■ 選んだ理由

センスの良さが際立っていました。ファッション分野のLPなので、細部にまで満足のいくデザインに巡り会えたのはとてもありがたいことだと感じています。

■ 提案者全員のお礼・コメント

この度は優れたデサインを多数ご提案いただきまして、誠にありがとうございました。レベルが高く、選ぶのが大変でしたがとても満足のいくコンペになりました。また機会がありましたら宜しくお願いいたします。

```html
<!DOCTYPE html>
<html lang="ja">
<head>
<meta charset="utf-8">
<title>Aoren Styling — 経営者のための戦略スタイリングサービス</title>
<link href="https://fonts.googleapis.com/css2?family=Noto+Serif+JP:wght@400;600;700&family=Noto+Sans+JP:wght@400;500&family=Cormorant+Garamond:wght@500;600&display=swap" rel="stylesheet">
<style>
  :root {
    --paper: #f4f2ee;
    --white: #ffffff;
    --ink: #2b2b2b;
    --muted: #6d6a65;
    --gold: #b39558;
    --gold-soft: #cdb585;
    --navy: #1d3562;
    --blue: #2e5c97;
    --charcoal: #26282b;
    --photo-warm: #b8a58c;
    --photo-deep: #6f5f4c;
  }
  * { box-sizing: border-box; margin: 0; padding: 0; }
  html, body { width: 870px; height: 1200px; overflow: hidden; background: var(--paper); }
  body { font-family: "Noto Sans JP", sans-serif; color: var(--ink); }

  .screen { position: absolute; left: 35px; width: 800px; background: var(--white); overflow: hidden; box-shadow: 0 2px 10px rgba(0,0,0,.08); }
  .screen--hero { top: 30px; height: 540px; }
  .screen--stylist { top: 600px; height: 570px; }

  .brand { display: flex; align-items: center; gap: 8px; }
  .brand__mark { width: 22px; height: 22px; border-radius: 50%; background: var(--ink); }
  .brand__name { font-family: "Cormorant Garamond", serif; font-weight: 600; font-size: 20px; letter-spacing: .02em; }
  .tagline { font-size: 10px; color: var(--muted); margin-left: 14px; }

  /* Hero screen */
  .site-header { height: 52px; display: flex; align-items: center; padding: 0 26px; background: var(--white); }
  .hero { position: relative; height: 420px; background: var(--gold); }
  .hero__photo { position: absolute; left: 150px; top: 0; width: 500px; height: 420px;
    background: linear-gradient(180deg, var(--photo-warm), var(--photo-deep)); }
  .hero__lead { position: absolute; left: 230px; top: 40px; width: 340px; padding: 6px 0; text-align: center;
    background: rgba(255,255,255,.85); font-family: "Noto Serif JP", serif; font-size: 12px; color: var(--ink); }
  .hero__title { position: absolute; left: 260px; top: 110px; width: 280px; text-align: center;
    font-family: "Noto Serif JP", serif; font-weight: 700; font-size: 30px; line-height: 1.45; color: var(--white); }
  .hero__title .num { font-size: 36px; }
  .hero__badge { position: absolute; left: 290px; top: 230px; width: 220px; padding: 14px 0; text-align: center;
    background: var(--blue); color: var(--white); font-family: "Noto Serif JP", serif; font-size: 14px; line-height: 1.7; }
  .hero-footer { height: 68px; display: flex; align-items: center; padding: 0 26px; border-top: 1px solid #e5e1da; }

  /* Stylist screen */
  .nav-bar { height: 50px; background: var(--charcoal); display: flex; align-items: center; padding: 0 26px; color: var(--white); }
  .nav-bar .tagline { color: #bdb9b2; }
  .steps { display: flex; background: var(--white); border-bottom: 1px solid #e5e1da; }
  .step { flex: 1; height: 58px; display: flex; flex-direction: column; align-items: center; justify-content: center; border-right: 1px solid #ece8e1; }
  .step__num { font-family: "Cormorant Garamond", serif; font-size: 24px; color: var(--ink); line-height: 1; }
  .step__label { font-size: 7px; color: var(--muted); margin-top: 4px; }
  .step--active { background: var(--gold); }
  .step--active .step__num, .step--active .step__label { color: var(--white); }

  .stylist { position: relative; height: 462px; background: var(--white); }
  .stylist__panel { position: absolute; right: 0; top: 0; width: 330px; height: 462px; }
  .stylist__index { position: absolute; right: 70px; top: 40px; text-align: center; color: var(--white); }
  .stylist__index .big { font-family: "Cormorant Garamond", serif; font-size: 96px; line-height: 1; color: var(--gold-soft); }
  .stylist__index .word { font-family: "Cormorant Garamond", serif; font-size: 18px; letter-spacing: .1em; color: var(--gold-soft); }
  .stylist__photo { position: absolute; left: 20px; top: 160px; width: 140px; height: 300px;
    background: linear-gradient(180deg, #9aa5b8, var(--navy)); }
  .stylist__body { position: absolute; left: 200px; top: 40px; width: 280px; }
  .stylist__title { font-family: "Noto Serif JP", serif; font-weight: 700; font-size: 20px; line-height: 1.6; color: var(--gold); }
  .stylist__text { margin-top: 18px; font-size: 10px; line-height: 2; color: var(--muted); }
  .books { display: flex; gap: 10px; margin-top: 22px; }
  .book { width: 54px; height: 74px; background: linear-gradient(180deg, #dfe4ec, #8a9ab3); }
</style>
</head>
<body>

<section class="screen screen--hero">
  <header class="site-header">
    <div class="brand"><span class="brand__mark"></span><span class="brand__name">Aoren Styling</span></div>
    <span class="tagline">経営者・専門家のための戦略的スタイリングサービス</span>
  </header>
  <div class="hero">
    <div class="hero__photo" role="img" aria-label="スーツ姿のスタイリストが立つ、トルソーや洋服の並ぶアトリエの写真"></div>
    <p class="hero__lead">スタイリング・ブランディングで経営者の価値を高める</p>
    <h1 class="hero__title">約<span class="num">300</span>名以上が<br>センスのいい経営者</h1>
    <p class="hero__badge">経営者のための<br>戦略スタイリングサービス</p>
  </div>
  <footer class="hero-footer">
    <div class="brand"><span class="brand__mark"></span><span class="brand__name">Aoren Styling</span></div>
    <span class="tagline">経営者・専門家のための戦略的スタイリングサービス</span>
  </footer>
</section>

<section class="screen screen--stylist">
  <header class="nav-bar">
    <div class="brand"><span class="brand__mark" style="background:var(--white)"></span><span class="brand__name">Aoren Styling</span></div>
    <span class="tagline">経営者・専門家のための戦略的スタイリングサービス</span>
  </header>
  <nav class="steps">
    <div class="step"><span class="step__num">01</span><span class="step__label">concept</span></div>
    <div class="step"><span class="step__num">02</span><span class="step__label">about</span></div>
    <div class="step"><span class="step__num">03</span><span class="step__label">reason</span></div>
    <div class="step step--active"><span class="step__num">04</span><span class="step__label">stylist</span></div>
    <div class="step"><span class="step__num">05</span><span class="step__label">voice</span></div>
    <div class="step"><span class="step__num">06</span><span class="step__label">case</span></div>
    <div class="step"><span class="step__num">07</span><span class="step__label">menu</span></div>
    <div class="step"><span class="step__num">08</span><span class="step__label">price</span></div>
    <div class="step"><span class="step__num">09</span><span class="step__label">flow</span></div>
    <div class="step"><span class="step__num">10</span><span class="step__label">faq</span></div>
    <div class="step"><span class="step__num">11</span><span class="step__label">media</span></div>
    <div class="step"><span class="step__num">12</span><span class="step__label">contact</span></div>
  </nav>
  <div class="stylist">
    <svg class="stylist__panel" viewBox="0 0 330 462" preserveAspectRatio="none" aria-hidden="true">
      <polygon points="120,0 330,0 330,462 0,462" fill="var(--navy)"/>
      <polygon points="0,462 120,0 126,0 8,462" fill="var(--gold)"/>
    </svg>
    <div class="stylist__index"><div class="big">04</div><div class="word">stylist</div></div>
    <div class="stylist__photo" role="img" aria-label="椅子に腰掛けたネイビースーツのスタイリストの写真"></div>
    <div class="stylist__body">
      <h2 class="stylist__title">300人以上の経営者の<br>ブランディングを手掛けた<br>ファッションのプロ</h2>
      <p class="stylist__text">はじめまして。スタイリストの代表です。<br>私はこれまで多くの経営者の装いを担当し、<br>ファッションを通じてブランディングを支援してきました。<br>今では書籍やメディアでも発信しています。</p>
      <div class="books">
        <div class="book" role="img" aria-label="著書の表紙"></div>
        <div class="book" role="img" aria-label="著書の表紙"></div>
        <div class="book" role="img" aria-label="掲載雑誌の表紙"></div>
        <div class="book" role="img" aria-label="掲載雑誌の表紙"></div>
      </div>
    </div>
  </div>
</section>

</body>
</html>
```